依頼詳細
表面はカラー、裏面は白黒で申し込み用紙にしようと考えています。
魅力のあるツアーだと思いますので、読み手に伝わるよう作成をお願いします。
〈ツアーのポイント〉
・透き通った青い海、緑の山々、満天の星空など、大自然に囲まれたダイナミックな眺望
・貸切バスで観光スポットをご案内
・地元の食材にこだわった料理を堪能
・島人との交流
・自然の中でBBQ、キャンプファイヤー
・宿泊は神津島唯一の温泉宿
・カップル成立で特典付き
・格安
など
多少変更が出るかもしれませんので、こちらでも編集できる形式で納品をお願いします。
ご不明点などありましたらご連絡ください。
よろしくお願いいたします。
記載項目
表現など変更して頂いて結構です。

【表面】
独身女性参加者募集
〈イベント名称〉渚トーク星結び
〈日時〉2015年7月3日(金)~2015年7月5日(日)
〈会場〉神津島
〈ツアースケジュール〉
1日目 20:00 東京 灯波客船ターミナル集合(女性のみ)・女子会
23:00 出航(大型客船)
2日目 9:00 神津島着・チェックイン
朝 男性合流・アイスブレイク
昼 昼食・島内観光
夜 BBQ・キャンプファイヤー・温泉旅館宿泊
3日目 朝 自由時間
13:35 神津島発
17:30 東京 灯波客船ターミナル着・解散
〈ツアーのポイント〉依頼詳細参考
〈集合場所〉白浪航路灯波港 1階ロビー ※若葉環状線蓮見坂駅から徒歩8分
〈集合時間〉2015年7月3日(金)20:00
〈参加対象〉20歳~35歳の島外在住独身女性
〈募集人数〉15名(先着順)
〈参加料金〉15,000円/1人(交通費・宿泊費・食費込み)
〈申込方法〉裏面の申込書にご記入の上、メール・FAX・郵送にてお申込みください。
〈申込締切〉2015年6月7日(日)
〈ホームページ〉
※ホームページのURLを載せたいのですが、まだ出来上がっていないので後ほどURLを追加できるようにしていただきたいです。

裏面は補足情報に記載します。
サイズ
A4
ページ数
両面
希望イメージ
• +5 0 +5
• シンプル
複雑
• 単色
カラフル
• 暗い
明るい
• 日常
高級
• 遊び心
厳粛
• 未来的
伝統的
• 女性的
男性的
希望する色
赤系、水色系、緑系、黄・オレンジ系
納品ファイル
補足説明
【裏面】申込用紙
〈イベント名称〉
〈日時〉
〈会場〉
〈募集人数〉15名(先着順)
〈参加資格〉20歳から35歳までの神津島外在住の独身女性
お一人様参加・シングルマザー・結婚歴あり歓迎
〈参加料金〉
MAIL  shiomi@hx.nagisanet-example.jp
メールでのお申し込みは①氏名②生年月日③住所④電話番号⑤メールアドレスを添えて上記のアドレスまでご送信ください。
FAX 04992-7-5530
〈申し込みフォーム〉
・氏名(ふりがな)
・氏名
・生年月日
・電話番号
・メールアドレス
・自己PR
〈注意事項〉
1 申し込み・キャンセルは6月7日(日)までにお願いします。
2 男女比は出来る限り調整しますが同数にならないこともありますのでご了承願います。
3 個人情報は厳重に管理し、本事業のみの使用とさせていただきます。
4 悪天候時はプログラム内容を変更または中止する場合があります。

申し込み受付後、事務局より順次詳細をお送りいたします。

問い合わせ・お申込み 汐見村商工会青年部事務局
〒100-0999 東京都汐見村汐見村2483番地
TEL  04992-7-4418
FAX  04992-7-5530

依頼公開後の追記内容
写真を添付します。

ターゲット層を対象にアンケート調査を実施した結果、最も多く票が集まったため。

この度は私どもの為に、多数ご提案をご用意していただき、誠にありがとうございます。どの提案も魅力を感じていましたが、上記の理由から一社選ばせていただきました。
折角親身にお世話をしていただいたところ、心苦しい限りですが、ご理解いただければ幸いです。
また、同様の機会があればよろしくお願いいたします。

```html
<!DOCTYPE html>
<html lang="ja">
<head>
<meta charset="utf-8">
<title>渚トーク星結び 独身女性参加者募集</title>
<link rel="stylesheet" href="https://fonts.googleapis.com/css2?family=Kiwi+Maru:wght@500&family=M+PLUS+Rounded+1c:wght@400;700;800&family=Pacifico&display=swap">
<style>
:root{
  --red:#e0353a;
  --pink:#f06a8a;
  --navy:#1d3a6b;
  --sea:#2f8fd0;
  --sky:#bfe4f5;
  --paper:#f7fbfd;
  --sand:#f2e2bf;
  --sand-dark:#d9c296;
  --green:#3f9a55;
  --ink:#333;
}
*{margin:0;padding:0;box-sizing:border-box}
html,body{width:849px;height:1200px;overflow:hidden}
body{background:#fff;font-family:"M PLUS Rounded 1c",sans-serif;color:var(--ink)}
.poster{position:relative;width:849px;height:1200px;background:linear-gradient(#e6f5fb 0,var(--paper) 320px);overflow:hidden}
.abs{position:absolute}
.bunting{left:0;top:0;width:849px;height:42px;background:linear-gradient(90deg,#e0353a 0 12%,#f4c430 12% 25%,#2f8fd0 25% 38%,#3f9a55 38% 50%,#e0353a 50% 62%,#f4c430 62% 75%,#2f8fd0 75% 88%,#3f9a55 88%);opacity:.35}
.tagline{top:14px;left:24px;color:var(--red);font-weight:800;font-size:21px;letter-spacing:1px}
.recruit{top:14px;right:26px;color:var(--red);font-weight:800;font-size:21px;letter-spacing:1px}
.banner{left:70px;top:52px;width:680px;height:112px}
.romaji{left:0;width:849px;top:58px;text-align:center;font-family:"Pacifico",cursive;color:var(--sea);font-size:20px}
.title{left:0;width:820px;top:84px;text-align:center;font-family:"Kiwi Maru",serif;font-size:60px;color:var(--navy);letter-spacing:2px;line-height:1}
.badge{left:726px;top:60px;width:112px;height:112px;border-radius:50%;background:var(--pink);color:#fff;text-align:center;font-weight:800;border:3px solid #fff;box-shadow:0 0 0 2px var(--pink)}
.badge .a{display:block;margin-top:14px;font-size:20px}
.badge .n{display:block;font-size:42px;line-height:40px}
.badge .b{font-size:18px}
.target{top:172px;left:0;width:849px;text-align:center;color:var(--green);font-weight:800;font-size:22px}
.date{top:205px;left:0;width:849px;text-align:center;color:var(--red);font-weight:800;line-height:1}
.date .yr{font-size:20px;vertical-align:top;margin-right:6px}
.date .big{font-size:56px}
.date .dow{display:inline-block;width:34px;height:34px;border-radius:50%;background:var(--red);color:#fff;font-size:20px;line-height:34px;vertical-align:middle;margin:0 4px}
.fee{top:274px;left:0;width:849px;text-align:center;color:var(--navy);font-weight:700;font-size:20px}
.fee strong{color:var(--red);font-size:28px}
.sched{left:18px;top:318px;width:813px;height:558px;background:#fff;border:3px solid var(--sky);border-radius:14px}
.sched-head{left:18px;top:302px;background:var(--sea);color:#fff;font-family:"Pacifico",cursive;font-size:24px;padding:2px 24px 6px;border-radius:10px 10px 10px 0}
.meet{left:36px;top:356px;width:440px;font-size:14px;font-weight:700;color:var(--navy);line-height:1.5}
.day{left:36px;width:440px}
.day .tag{position:absolute;left:0;top:0;width:62px;height:62px;border-radius:50%;background:var(--sea);color:#fff;text-align:center;font-weight:800;font-size:18px;line-height:62px}
.day.d2 .tag{background:var(--green)}
.day.d3 .tag{background:#f0a020}
.day ul{list-style:none;margin-left:76px;font-size:15px;font-weight:700;line-height:1.75;padding-top:4px}
.day li span{display:inline-block;width:52px;color:var(--sea)}
.couple{left:36px;top:730px;color:var(--red);font-weight:800;font-size:33px;letter-spacing:2px}
.photo{border-radius:8px;border:3px solid #fff;box-shadow:0 1px 4px rgba(0,0,0,.25)}
.cap{font-size:12px;font-weight:700;color:var(--navy);background:#fff;padding:1px 6px;border-radius:8px}
.waves{left:0;top:880px;width:849px;height:320px}
.points{left:0;top:918px;width:849px;text-align:center;font-size:15px;font-weight:700;color:var(--navy)}
.url{left:0;top:1040px;width:849px;text-align:center;font-family:"Pacifico",cursive;font-size:48px;color:var(--navy);letter-spacing:2px}
.apply{left:0;top:1148px;width:849px;text-align:center;color:#fff;font-weight:700;font-size:16px}
</style>
</head>
<body>
<div class="poster">
  <div class="abs bunting" role="img" aria-label="色とりどりの三角旗の飾り"></div>
  <div class="abs tagline">神々が集う島</div>
  <div class="abs recruit">独身女性参加者募集</div>

  <svg class="abs banner" viewBox="0 0 680 112" aria-hidden="true">
    <polygon points="0,30 60,30 60,100 0,100 22,65" fill="var(--sand-dark)"/>
    <polygon points="680,30 620,30 620,100 680,100 658,65" fill="var(--sand-dark)"/>
    <path d="M40,8 Q340,-6 640,8 L640,96 Q340,82 40,96 Z" fill="var(--sand)" stroke="#c9ae7c" stroke-width="2"/>
  </svg>
  <div class="abs romaji">kouzushima</div>
  <div class="abs title">渚トーク星結び</div>
  <div class="abs badge"><span class="a">先着</span><span class="n">15</span><span class="b">名</span></div>

  <div class="abs target">（参加対象）20歳～35歳の島外在住独身女性</div>
  <div class="abs date"><span class="yr">2015年</span><span class="big">7月3日</span><span class="dow">金</span><span class="big">～7月5日</span><span class="dow">日</span></div>
  <div class="abs fee">参加料金 <strong>15,000円</strong>/1人（交通費・宿泊費・食費込み）</div>

  <div class="abs sched"></div>
  <div class="abs sched-head">tourschedule</div>
  <div class="abs meet">（集合場所）白浪航路灯波港 1階ロビー<br>※若葉環状線蓮見坂駅から徒歩8分</div>

  <div class="abs day d1" style="top:412px">
    <div class="tag">1日目</div>
    <ul>
      <li><span>20:00</span>東京 灯波客船ターミナル集合（女性のみ）・女子会</li>
      <li><span>23:00</span>出航（大型客船）</li>
    </ul>
  </div>
  <div class="abs day d2" style="top:500px">
    <div class="tag">2日目</div>
    <ul>
      <li><span>9:00</span>神津島着・チェックイン</li>
      <li><span>朝</span>男性合流・アイスブレイク</li>
      <li><span>昼</span>昼食・島内観光</li>
      <li><span>夜</span>BBQ・キャンプファイヤー・温泉旅館宿泊</li>
    </ul>
  </div>
  <div class="abs couple">カップル成立特典あり！！</div>
  <div class="abs day d3" style="top:790px">
    <div class="tag">3日目</div>
    <ul>
      <li><span>朝</span>自由時間　<span>13:35</span>神津島発</li>
      <li><span>17:30</span>東京 灯波客船ターミナル着・解散</li>
    </ul>
  </div>

  <div class="abs photo" style="left:600px;top:336px;width:216px;height:120px;background:linear-gradient(#1c2d5a,#3a5a9a)" role="img" aria-label="満天の星空の写真"></div>
  <div class="abs cap" style="left:610px;top:430px">満天の星</div>
  <div class="abs photo" style="left:520px;top:470px;width:150px;height:120px;background:linear-gradient(#7fd0f0,#1f8ac4)" role="img" aria-label="透き通った青い海の写真"></div>
  <div class="abs cap" style="left:528px;top:565px">澄んだ海</div>
  <div class="abs photo" style="left:680px;top:478px;width:136px;height:110px;background:linear-gradient(135deg,#e85a3a,#c22a20)" role="img" aria-label="地元の食材を使った料理の写真"></div>
  <div class="abs cap" style="left:688px;top:562px">島の味覚</div>
  <div class="abs photo" style="left:560px;top:612px;width:256px;height:130px;background:linear-gradient(#9fd6ee,#5aa86a)" role="img" aria-label="緑の山々と海岸の風景写真"></div>
  <div class="abs photo" style="left:600px;top:756px;width:216px;height:108px;background:linear-gradient(#d8c6a8,#8a6e50)" role="img" aria-label="温泉宿の写真"></div>
  <div class="abs cap" style="left:608px;top:838px">温泉宿</div>

  <svg class="abs waves" viewBox="0 0 849 320" preserveAspectRatio="none" aria-hidden="true">
    <path d="M0,20 Q53,0 106,20 T212,20 T318,20 T424,20 T530,20 T636,20 T742,20 T849,20 V320 H0Z" fill="#dff1fa"/>
    <path d="M0,120 Q53,95 106,120 T212,120 T318,120 T424,120 T530,120 T636,120 T742,120 T849,120 V320 H0Z" fill="#eaf7fd"/>
    <path d="M0,250 Q53,228 106,250 T212,250 T318,250 T424,250 T530,250 T636,250 T742,250 T849,250 V320 H0Z" fill="var(--sea)"/>
  </svg>
  <div class="abs points">透き通った青い海、緑の山々、満天の星空など、大自然に囲まれたダイナミックな眺望</div>
  <div class="abs url">http://**************</div>
  <div class="abs apply">裏面の申込書にご記入の上、メール・FAX・郵送にてお申込みください。</div>
</div>
</body>
</html>
```